Sell Sheet for Food Topping Applicator Manufacturer, Primarily Frozen Pizza, Tray Meals, Bakery i...

Sell sheet-2 sided w front showing machine photo, sell points. Back page listing some specs and technical information/photos. RXP7B attachment shows what we currently have - we are looking for a new, fresh look.
We like the look of the file attached, Venlo Cascade Topping Applicator, so we'd like something with this clean look.

Target Market(s)

Food Processing Industry

Industry/Entity Type

Machinery

Font styles to use
Serif

Colors
3176b5

Requirements
Must have
• Should be clean looking. Our logo present. Selling points, possibly in paragraph form on front, Back page to have specs, some drawings of machine. We currently use blue, gray, white and black colors.

```html
<!DOCTYPE html>
<html lang="en">
<head>
<meta charset="utf-8">
<title>Norvale Sell Sheet – RXP7B</title>
<link href="https://fonts.googleapis.com/css2?family=Michroma&family=Open+Sans:wght@400;600;700&display=swap" rel="stylesheet">
<style>
:root{
  --bg:#2e2e30;
  --sheet:#232426;
  --blue:#3a8fd8;
  --blue-deep:#3176b5;
  --white:#f1f2f4;
  --grey:#9a9da3;
  --rule:#3c4d63;
}
*{box-sizing:border-box;margin:0;padding:0}
html,body{width:1200px;height:776px;overflow:hidden;background:var(--bg)}
body{font-family:"Open Sans",Arial,sans-serif;color:var(--white);position:relative}
.sheet{position:absolute;top:20px;width:570px;height:736px;background:var(--sheet);box-shadow:0 6px 18px rgba(0,0,0,.45)}
.front{left:20px}
.back{left:610px}
.brand{position:absolute;top:22px;right:26px;text-align:center}
.brand-name{display:flex;align-items:center;gap:6px;font-family:"Michroma",sans-serif;font-size:12px;letter-spacing:3px;color:var(--blue)}
.brand-dot{width:7px;height:7px;border-radius:50%;background:var(--blue)}
.brand-url{font-size:7px;letter-spacing:2px;color:var(--blue);margin-top:2px}
.machine-photo{position:absolute;left:22px;top:50px;width:250px;height:300px;background:radial-gradient(circle at 50% 45%,#8d9096,#4a4d52 60%,#232426 100%)}
.photo-caption{position:absolute;left:22px;top:362px;width:250px;text-align:center;font-size:10.5px;color:var(--white);line-height:1.3}
.product-title{position:absolute;left:292px;top:76px;font-family:"Michroma",sans-serif;font-size:12px;line-height:1.7;color:var(--blue);font-variant:small-caps;letter-spacing:1px}
.product-intro{position:absolute;left:292px;top:168px;width:252px;font-size:10.5px;line-height:1.3;color:var(--white)}
.drawings{position:absolute;left:268px;top:330px;width:282px;height:300px;background:linear-gradient(160deg,#26303d,#1f2a38);border:1px solid #2b3b50}
.company{position:absolute;left:30px;top:440px;width:230px}
.company-name{font-family:"Michroma",sans-serif;font-size:22px;letter-spacing:6px;color:var(--blue);padding-bottom:6px;border-bottom:1px solid var(--blue-deep)}
.company-text{margin-top:10px;font-family:"Michroma",sans-serif;font-size:10.5px;line-height:2.05;letter-spacing:1.5px;font-variant:small-caps;color:var(--white)}
.contact{position:absolute;left:0;right:0;bottom:0;height:70px;border-top:1px solid var(--rule);display:flex;align-items:center;gap:24px;padding:0 28px;font-size:11.5px}
.contact-label{font-family:"Open Sans",sans-serif;font-weight:700;font-size:15px;color:var(--blue);letter-spacing:1px}
.contact-item{display:flex;align-items:center;gap:7px}
.contact-item svg{width:18px;height:18px;fill:var(--blue)}
.spec-heading{position:absolute;left:30px;top:40px;font-size:18px;font-weight:700;color:var(--blue);letter-spacing:1px;padding-bottom:4px;border-bottom:1px solid var(--blue-deep)}
.spec-products{position:absolute;left:46px;top:80px;font-size:12px}
.spec-products h3{font-size:13px;color:var(--blue);font-weight:700;letter-spacing:.5px}
.spec-products small{font-size:8.5px}
.spec-col{position:absolute;top:126px;display:flex;flex-direction:column;gap:22px}
.col-left{left:26px;width:260px}
.col-right{left:298px;width:250px}
.spec{display:flex;gap:10px}
.spec-tick{width:18px;height:18px;flex:none;margin-top:2px}
.spec-body{border-left:1px solid var(--grey);padding-left:8px;padding-top:2px}
.spec h3{font-size:13px;font-weight:700;color:var(--blue);letter-spacing:.8px;text-transform:uppercase;line-height:1.15}
.spec p{font-size:10.5px;line-height:1.3;margin-top:4px}
.spec p.tiny{font-size:8px;line-height:1.25}
</style>
</head>
<body>

<section class="sheet front">
  <div class="brand"><div class="brand-name"><span class="brand-dot"></span>NORVALE</div><div class="brand-url">WWW.NRV-TS.COM</div></div>
  <div class="machine-photo" role="img" aria-label="Photo of the stainless steel RXP7B sauce applicator on casters with hopper and blue conveyor"></div>
  <p class="photo-caption">RXP7B shown with optional hopper<br>Level Control System</p>
  <h1 class="product-title">Conveyorized Aimline™<br>Sauce Applicator<br>Model# RXP7B</h1>
  <p class="product-intro">USDA Compliant, patented sauce applicator, capable of evenly applying sauce to your product while maintaining a sauce free border. Our CONVEYORIZED AIMLINE™ sauce applicator is simple easy to use system. Your pizzas is precisely located under applicating head by means of our conveyor. When in position the sauce is automatically applied.</p>
  <div class="drawings" role="img" aria-label="Technical line drawings of the machine with front, side and perspective views and dimensions"></div>
  <div class="company">
    <h2 class="company-name">NORVALE</h2>
    <p class="company-text">Norvale manufactures high speed automated topping equipment. We offer standard production systems as well as custom engineered solutions.</p>
  </div>
  <footer class="contact">
    <span class="contact-label">CONTACT US:</span>
    <span class="contact-item"><svg viewBox="0 0 24 24"><path d="M6.6 10.8a15 15 0 0 0 6.6 6.6l2.2-2.2a1 1 0 0 1 1-.25 11.4 11.4 0 0 0 3.6.57 1 1 0 0 1 1 1V20a1 1 0 0 1-1 1A17 17 0 0 1 3 4a1 1 0 0 1 1-1h3.5a1 1 0 0 1 1 1c0 1.25.2 2.45.57 3.57a1 1 0 0 1-.25 1z"/></svg>+1 555.210.4870</span>
    <span class="contact-item"><svg viewBox="0 0 24 24"><path d="M2 5h20v14H2zm2 2v.5l8 5 8-5V7z"/></svg>INFO@NRV-TS.COM</span>
    <span class="contact-item"><svg viewBox="0 0 24 24"><circle cx="12" cy="12" r="10"/></svg>WWW.NRV-TS.COM</span>
  </footer>
</section>

<section class="sheet back">
  <div class="brand"><div class="brand-name"><span class="brand-dot"></span>NORVALE</div><div class="brand-url">WWW.NRV-TS.COM</div></div>
  <h2 class="spec-heading">SPECIFICATIONS</h2>
  <div class="spec-products"><h3>PRODUCTS:</h3>Rigid and Supported Products : <small>Square, Rectangular and Round Up To18"</small></div>

  <div class="spec-col col-left">
    <div class="spec"><svg class="spec-tick" viewBox="0 0 20 20"><path d="M17 6A8 8 0 1 1 12 2.3" fill="none" stroke="#3a8fd8" stroke-width="1.6"/><path d="M5 9l4 4 9-10" fill="none" stroke="#3a8fd8" stroke-width="2.2"/></svg>
      <div class="spec-body"><h3>Sauce:</h3><p class="tiny">Flowable Product with All Particulate<br>Flowable Product with All Particulate<br>Able to Pass Through a 3/32 (2mm)<br>Diameter Hole Screen.Larger<br>Particulates Possible on custom<br>Designed Patterns.</p></div></div>
    <div class="spec"><svg class="spec-tick" viewBox="0 0 20 20"><path d="M17 6A8 8 0 1 1 12 2.3" fill="none" stroke="#3a8fd8" stroke-width="1.6"/><path d="M5 9l4 4 9-10" fill="none" stroke="#3a8fd8" stroke-width="2.2"/></svg>
      <div class="spec-body"><h3>Portion:</h3><p>0,5oz.(14g).10oz.(284g)<br>+/- 0.2oz.(6g)</p></div></div>
    <div class="spec"><svg class="spec-tick" viewBox="0 0 20 20"><path d="M17 6A8 8 0 1 1 12 2.3" fill="none" stroke="#3a8fd8" stroke-width="1.6"/><path d="M5 9l4 4 9-10" fill="none" stroke="#3a8fd8" stroke-width="2.2"/></svg>
      <div class="spec-body"><h3>Standard Patterns:</h3><p>0.5in (12.7mm) Increments<br>Custom Patterns Also Available</p></div></div>
    <div class="spec"><svg class="spec-tick" viewBox="0 0 20 20"><path d="M17 6A8 8 0 1 1 12 2.3" fill="none" stroke="#3a8fd8" stroke-width="1.6"/><path d="M5 9l4 4 9-10" fill="none" stroke="#3a8fd8" stroke-width="2.2"/></svg>
      <div class="spec-body"><h3>Drive System:</h3><p>Convoyer Utilizes a Precision Elecric<br>Drive Motor Washdown Capable</p></div></div>
    <div class="spec"><svg class="spec-tick" viewBox="0 0 20 20"><path d="M17 6A8 8 0 1 1 12 2.3" fill="none" stroke="#3a8fd8" stroke-width="1.6"/><path d="M5 9l4 4 9-10" fill="none" stroke="#3a8fd8" stroke-width="2.2"/></svg>
      <div class="spec-body"><h3>Frame:</h3><p>Stainless Steel  Frame Locking Swivel<br>Casters with No Exposed Threads</p></div></div>
    <div class="spec"><svg class="spec-tick" viewBox="0 0 20 20"><path d="M17 6A8 8 0 1 1 12 2.3" fill="none" stroke="#3a8fd8" stroke-width="1.6"/><path d="M5 9l4 4 9-10" fill="none" stroke="#3a8fd8" stroke-width="2.2"/></svg>
      <div class="spec-body"><h3>Penumatic:</h3><p>80 PSIG @ 6 SCFM Clean Dry Air</p></div></div>
  </div>

  <div class="spec-col col-right">
    <div class="spec"><svg class="spec-tick" viewBox="0 0 20 20"><path d="M17 6A8 8 0 1 1 12 2.3" fill="none" stroke="#3a8fd8" stroke-width="1.6"/><path d="M5 9l4 4 9-10" fill="none" stroke="#3a8fd8" stroke-width="2.2"/></svg>
      <div class="spec-body"><h3>Production Rates<br>(Up To):</h3><p class="tiny">PRODUCTION RATES (UP TO):<br>6" @110+Pizzas Per Minute, 6,600+ Per Hour<br>8" @110+Pizzas Per Minute, 6,600+ Per Hour<br>10" @ 96 Pizzas Per Minute, 5,760 Per Hour<br>12" @ 80 Pizzas Per Minute, 4,800 Per Hour<br>14" @ 68 Pizzas Per Minute, 4,080 Per Hour<br>16" @ 60 Pizzas Per Minute, 3,600 Per Hour</p></div></div>
    <div class="spec"><svg class="spec-tick" viewBox="0 0 20 20"><path d="M17 6A8 8 0 1 1 12 2.3" fill="none" stroke="#3a8fd8" stroke-width="1.6"/><path d="M5 9l4 4 9-10" fill="none" stroke="#3a8fd8" stroke-width="2.2"/></svg>
      <div class="spec-body"><h3>Hopper:</h3><p>12 gallon Hopper (45.4 Liters)<br>(approx)</p></div></div>
    <div class="spec"><svg class="spec-tick" viewBox="0 0 20 20"><path d="M17 6A8 8 0 1 1 12 2.3" fill="none" stroke="#3a8fd8" stroke-width="1.6"/><path d="M5 9l4 4 9-10" fill="none" stroke="#3a8fd8" stroke-width="2.2"/></svg>
      <div class="spec-body"><h3>Controls:</h3><p>7" Color Touch Screen</p></div></div>
    <div class="spec"><svg class="spec-tick" viewBox="0 0 20 20"><path d="M17 6A8 8 0 1 1 12 2.3" fill="none" stroke="#3a8fd8" stroke-width="1.6"/><path d="M5 9l4 4 9-10" fill="none" stroke="#3a8fd8" stroke-width="2.2"/></svg>
      <div class="spec-body"><h3>Cantilevered Conveyor</h3><p>Polyurethane Flat Belt 1 1/2" Pulley<br>Diamatter Removable conveyor</p></div></div>
    <div class="spec"><svg class="spec-tick" viewBox="0 0 20 20"><path d="M17 6A8 8 0 1 1 12 2.3" fill="none" stroke="#3a8fd8" stroke-width="1.6"/><path d="M5 9l4 4 9-10" fill="none" stroke="#3a8fd8" stroke-width="2.2"/></svg>
      <div class="spec-body"><h3>Elecrical:</h3><p>220 Volts,1Phase, 5 AmpCircuit, 60 Hz<br>Stainless Steel Control Enclosure</p></div></div>
    <div class="spec"><svg class="spec-tick" viewBox="0 0 20 20"><path d="M17 6A8 8 0 1 1 12 2.3" fill="none" stroke="#3a8fd8" stroke-width="1.6"/><path d="M5 9l4 4 9-10" fill="none" stroke="#3a8fd8" stroke-width="2.2"/></svg>
      <div class="spec-body"><h3>Options:</h3><p>Hopper Level Pump and Level Control<br>Dual Lanes for Smaller Products<br>Start/Stop Introconnectivity<br>Stainless Steel Control Hopper</p></div></div>
  </div>

  <footer class="contact">
    <span class="contact-label">CONTACT US:</span>
    <span class="contact-item"><svg viewBox="0 0 24 24"><path d="M6.6 10.8a15 15 0 0 0 6.6 6.6l2.2-2.2a1 1 0 0 1 1-.25 11.4 11.4 0 0 0 3.6.57 1 1 0 0 1 1 1V20a1 1 0 0 1-1 1A17 17 0 0 1 3 4a1 1 0 0 1 1-1h3.5a1 1 0 0 1 1 1c0 1.25.2 2.45.57 3.57a1 1 0 0 1-.25 1z"/></svg>+1 555.210.4870</span>
    <span class="contact-item"><svg viewBox="0 0 24 24"><path d="M2 5h20v14H2zm2 2v.5l8 5 8-5V7z"/></svg>INFO@NRV-TS.COM</span>
    <span class="contact-item"><svg viewBox="0 0 24 24"><circle cx="12" cy="12" r="10"/></svg>WWW.NRV-TS.COM</span>
  </footer>
</section>

</body>
</html>
```